Quillmoor Homes Flyer

Quarter-page leave-behind flyer for a commercial cleaning company (print)

ABOUT US
Velto Commercial Cleaning is a Texas-owned commercial cleaning company serving Austin for over 20 years. We were recently named to Quillmoor Homes's Capital Partner Circle, a preferred vendor program covering apartment communities across the Austin metro. Our sales team will hand this flyer to apartment community managers during property visits.

THE JOB THIS FLYER MUST DO
A busy property manager should scan it in five seconds, understand what we do, trust us and keep the card on their desk. The call to action is booking a free walkthrough of their community. Do not include any pricing.

SPECS
Size: 4.25 x 5.5 inches (quarter of a letter page), single sided, portrait. Print ready with 0.125 inch bleed, CMYK, 300 dpi minimum. Vector preferred.

REQUIRED CONTENT
Headline: The clean your residents notice.
Badge or tagline: Quillmoor Homes's Approved Austin Cleaning Company.
Supporting line: Preferred Vendor Partner in QHM's Capital Partner Circle. Texas-owned, serving Austin for 20+ years.
Services (icons welcome): recurring janitorial, floor strip wax and buff, carpet extraction, windows and glass, upholstery care, pressure washing, move-in and move-out cleans, damage restoration.
Trust points: licensed and insured, background-checked crews, TrustLedger compliant, invoicing through Supplier Nook and Brixa Systems.

Social proof line: Already trusted by QHM communities. Ask your peers at The Harwick and The Olsen at Birchfield.

Call to action: Book a free walkthrough of your community. Call or email 512-555-0147 or support@veltocleaning.example

STYLE DIRECTION
Clean, crisp and premium. Whiteness and shine should feel like part of the message. We like a deep green and teal palette with one warm accent, but strong alternative directions are welcome. Custom icons over clip art.
AVOID
Stock photos of cleaners with buckets, cartoon mascots, sparkle overload, cluttered layouts, any prices or dollar amounts.
DELIVERABLES
Print-ready PDF with bleed and crop marks, plus editable source files (AI, PSD or Figma). A version with our logo placement marked, since we will supply the logo file to the winner.

```html
<!DOCTYPE html>
<html lang="en">
<head>
<meta charset="utf-8">
<title>Quillmoor Homes Flyer – Velto Commercial Cleaning</title>
<link href="https://fonts.googleapis.com/css2?family=Inter:wght@400;500;600;700;800&display=swap" rel="stylesheet">
<style>
  :root {
    --forest: #1c3a33;
    --forest-deep: #17322b;
    --teal: #2a9a80;
    --teal-line: #2f8f78;
    --gold: #f7c514;
    --white: #ffffff;
    --text-soft: #e8efec;
  }
  * { margin: 0; padding: 0; box-sizing: border-box; }
  html, body { width: 933px; height: 1200px; overflow: hidden; background: var(--forest); }
  .flyer {
    position: relative; width: 933px; height: 1200px; overflow: hidden;
    background: var(--forest); color: var(--white);
    font-family: "Inter", sans-serif;
  }
  .abs { position: absolute; }

  .hero-photo { position: absolute; top: 0; right: 0; width: 280px; height: 362px; }

  .headline {
    left: 55px; top: 32px; font-size: 67px; font-weight: 800;
    line-height: 78px; letter-spacing: -0.5px;
  }
  .headline .accent { color: var(--teal); }

  .badge {
    left: 0; top: 218px; width: 630px; height: 46px;
    background: var(--gold); border-radius: 0 23px 23px 0;
    display: flex; align-items: center; gap: 14px; padding-left: 18px;
    color: var(--forest); font-size: 19px; font-weight: 700; letter-spacing: -0.2px;
    white-space: nowrap;
  }

  .support { left: 57px; top: 288px; font-size: 18.5px; line-height: 29px; color: var(--text-soft); }
  .support strong { color: var(--white); font-weight: 700; }

  .section-title {
    left: 57px; top: 369px; font-size: 21px; font-weight: 700; letter-spacing: 0.2px;
  }
  .section-rule { left: 247px; top: 381px; right: 0; height: 2px; background: var(--gold); }

  .service { width: 220px; text-align: center; }
  .service-icon {
    display: block; margin: 0 auto; width: 120px; height: 120px;
    fill: none; stroke: var(--teal); stroke-width: 2.4;
    stroke-linecap: round; stroke-linejoin: round;
  }
  .service-label {
    margin-top: 25px; font-size: 16.5px; font-weight: 500; letter-spacing: 2.6px;
    line-height: 21px; text-transform: uppercase;
  }

  .trust-band {
    left: 0; top: 840px; width: 933px; height: 217px;
    background: var(--forest-deep);
    border-top: 2px solid var(--gold); border-bottom: 2px solid var(--teal-line);
  }
  .trust { width: 200px; text-align: center; top: 870px; }
  .trust svg { display: block; margin: 0 auto 14px; }
  .trust-label { font-size: 15.5px; font-weight: 700; line-height: 19px; letter-spacing: 0.5px; }

  .proof {
    left: 76px; top: 985px; padding-left: 19px;
    border-left: 3px solid var(--teal-line);
    font-size: 20px; line-height: 25px; letter-spacing: 0.6px;
  }
  .proof strong { font-weight: 700; }

  .cta {
    left: 0; width: 933px; top: 1080px; text-align: center;
    font-size: 34px; font-weight: 800; letter-spacing: 0.8px;
  }
  .cta .accent { color: var(--gold); }

  .contact { top: 1135px; display: flex; align-items: center; gap: 16px;
    font-size: 31px; font-weight: 700; letter-spacing: 1.5px; white-space: nowrap; }
  .contact-phone { left: 71px; }
  .contact-email { left: 388px; font-size: 25px; letter-spacing: 0.6px; top: 1138px; }
</style>
</head>
<body>
<main class="flyer">

  <svg class="hero-photo" viewBox="0 0 280 362" role="img" aria-label="Photo of two uniformed cleaners polishing a bright lobby floor">
    <defs>
      <linearGradient id="photoTone" x1="0" y1="0" x2="1" y2="1">
        <stop offset="0" stop-color="#dfe6e3"/>
        <stop offset="0.55" stop-color="#b9c7c1"/>
        <stop offset="1" stop-color="#8ea59c"/>
      </linearGradient>
    </defs>
    <path d="M0 0 H280 V362 H150 C70 362 30 300 22 210 C15 130 30 60 0 0 Z" fill="url(#photoTone)" stroke="#2a9a80" stroke-width="5"/>
  </svg>

  <h1 class="abs headline">The clean your<br>residents <span class="accent">notice</span></h1>

  <div class="abs badge">
    <svg width="24" height="24" viewBox="0 0 24 24" aria-hidden="true"><path d="M12 1 C13 9 15 11 23 12 C15 13 13 15 12 23 C11 15 9 13 1 12 C9 11 11 9 12 1 Z" fill="#1c3a33"/></svg>
    <span>Quillmoor Homes's Approved Austin Cleaning Company</span>
  </div>

  <p class="abs support">Preferred Vendor Partner in QHM's Capital Partner Circle.<br><strong>Texas-owned, serving Austin for 20+ years.</strong></p>

  <h2 class="abs section-title">OUR SERVICES</h2>
  <div class="abs section-rule"></div>

  <div class="abs service" style="left:14px; top:419px;">
    <svg class="service-icon" viewBox="0 0 120 120" role="img" aria-label="Broom and dustpan icon">
      <path d="M40 2 V86"/><path d="M30 86 H50 L58 118 H20 Z"/><path d="M28 102 L26 118 M36 100 L34 118 M44 100 L46 118 M52 102 L54 118"/>
      <path d="M88 48 V72 H78 L70 118 H116 L110 76 Q108 72 100 72 V48 Z"/>
      <path d="M70 20 L72 26 L78 28 L72 30 L70 36 L68 30 L62 28 L68 26 Z"/>
    </svg>
    <p class="service-label">Recurring<br>Janitorial</p>
  </div>
  <div class="abs service" style="left:228px; top:419px;">
    <svg class="service-icon" viewBox="0 0 120 120" role="img" aria-label="Floor buffer icon">
      <path d="M80 4 H112"/><path d="M96 4 L64 80"/><path d="M84 30 L74 54 L62 50 L72 26 Z"/>
      <ellipse cx="50" cy="96" rx="38" ry="12"/><path d="M22 88 V80 Q50 68 78 80 V88"/>
      <circle cx="90" cy="92" r="8"/><path d="M6 100 Q4 90 8 82 M112 104 Q108 112 98 116"/>
    </svg>
    <p class="service-label">Floor Strip<br>Wax and Buff</p>
  </div>
  <div class="abs service" style="left:466px; top:419px;">
    <svg class="service-icon" viewBox="0 0 120 120" role="img" aria-label="Carpet extraction wand icon">
      <path d="M4 110 L30 80 L46 96 L40 116 Z"/><path d="M34 84 L84 26"/><path d="M42 92 L90 34"/>
      <path d="M86 30 Q104 8 116 24 Q122 44 108 64 Q98 80 114 96"/>
      <path d="M60 62 L48 76 M48 76 H56 M48 76 V68"/>
    </svg>
    <p class="service-label">Carpet<br>Extraction</p>
  </div>
  <div class="abs service" style="left:695px; top:419px;">
    <svg class="service-icon" viewBox="0 0 120 120" role="img" aria-label="Window being wiped icon">
      <rect x="4" y="4" width="112" height="112"/><rect x="12" y="12" width="96" height="96"/>
      <path d="M64 12 L100 48 L56 92 L20 56"/><path d="M24 34 L40 18 M30 40 L38 32"/>
      <path d="M86 84 Q96 80 100 90 L106 112"/>
    </svg>
    <p class="service-label">Windows<br>and Glass</p>
  </div>

  <div class="abs service" style="left:14px; top:629px;">
    <svg class="service-icon" viewBox="0 0 120 120" role="img" aria-label="Armchair with brush icon">
      <path d="M20 60 V30 Q20 20 30 20 H96"/><path d="M20 60 Q4 56 4 70 Q4 82 20 80 V110 H116"/>
      <path d="M20 92 H116"/><path d="M116 2 L80 46"/><path d="M70 40 L92 58 L82 70 L60 52 Z"/>
      <path d="M64 60 L58 68 M70 64 L64 72 M76 68 L70 76"/>
    </svg>
    <p class="service-label">Upholstery<br>Care</p>
  </div>
  <div class="abs service" style="left:228px; top:629px;">
    <svg class="service-icon" viewBox="0 0 120 120" role="img" aria-label="Pressure washer wand icon">
      <path d="M6 78 L36 66 L44 80 L30 86 L34 110 L22 112 L16 88 L10 90 Z"/>
      <path d="M40 72 L92 40"/><path d="M44 80 Q60 96 50 112"/>
      <path d="M96 36 L116 18 M98 40 L118 32 M94 32 L104 10"/>
    </svg>
    <p class="service-label">Pressure<br>Washing</p>
  </div>
  <div class="abs service" style="left:446px; top:629px; width:260px;">
    <svg class="service-icon" viewBox="0 0 120 120" role="img" aria-label="Moving box with keys icon">
      <path d="M20 60 L60 44 L100 60 L60 76 Z"/><path d="M20 60 V100 L60 116 L100 100 V60"/>
      <path d="M60 76 V116"/><path d="M20 60 L8 74 L48 90 L60 76 L72 90 L112 74 L100 60"/>
      <circle cx="48" cy="14" r="7"/><path d="M48 21 V34 M48 28 H53"/>
      <circle cx="72" cy="14" r="7"/><path d="M72 21 V34 M72 28 H77"/>
    </svg>
    <p class="service-label">Move-in and<br>Move-out Cleans</p>
  </div>
  <div class="abs service" style="left:695px; top:629px;">
    <svg class="service-icon" viewBox="0 0 120 120" role="img" aria-label="Water and fire damage icon">
      <path d="M30 6 Q50 30 46 44 Q40 56 28 54 Q14 50 18 36 Q22 24 30 6 Z"/>
      <path d="M28 116 Q10 110 12 94 Q14 82 24 74 Q24 88 32 88 Q30 78 40 70 Q50 86 46 100 Q42 114 28 116 Z"/>
      <path d="M6 60 L16 70 M16 60 L6 70"/>
      <path d="M64 22 H110 L118 2"/><path d="M110 22 V98 L118 116"/><path d="M64 98 H110"/>
      <path d="M62 60 H92 M84 50 L94 60 L84 70"/>
    </svg>
    <p class="service-label">Damage<br>Restoration</p>
  </div>

  <div class="abs trust-band"></div>

  <div class="abs trust" style="left:24px;">
    <svg width="30" height="30" viewBox="0 0 30 30" aria-hidden="true"><circle cx="15" cy="15" r="13" fill="none" stroke="#2a9a80" stroke-width="2.4"/><path d="M9 15.5 L13.5 20 L22 9" fill="none" stroke="#2a9a80" stroke-width="2.6" stroke-linecap="round" stroke-linejoin="round"/></svg>
    <p class="trust-label">Licensed<br>and Insured</p>
  </div>
  <div class="abs trust" style="left:237px; width:200px;">
    <svg width="30" height="30" viewBox="0 0 30 30" aria-hidden="true"><circle cx="15" cy="15" r="13" fill="none" stroke="#2a9a80" stroke-width="2.4"/><path d="M9 15.5 L13.5 20 L22 9" fill="none" stroke="#2a9a80" stroke-width="2.6" stroke-linecap="round" stroke-linejoin="round"/></svg>
    <p class="trust-label">Background-Checked<br>Crews</p>
  </div>
  <div class="abs trust" style="left:476px;">
    <svg width="30" height="30" viewBox="0 0 30 30" aria-hidden="true"><circle cx="15" cy="15" r="13" fill="none" stroke="#2a9a80" stroke-width="2.4"/><path d="M9 15.5 L13.5 20 L22 9" fill="none" stroke="#2a9a80" stroke-width="2.6" stroke-linecap="round" stroke-linejoin="round"/></svg>
    <p class="trust-label">TrustLedger<br>Compliant</p>
  </div>
  <div class="abs trust" style="left:694px; width:220px;">
    <svg width="30" height="30" viewBox="0 0 30 30" aria-hidden="true"><circle cx="15" cy="15" r="13" fill="none" stroke="#2a9a80" stroke-width="2.4"/><path d="M9 15.5 L13.5 20 L22 9" fill="none" stroke="#2a9a80" stroke-width="2.6" stroke-linecap="round" stroke-linejoin="round"/></svg>
    <p class="trust-label">Invoicing Through<br>Supplier Nook and<br>Brixa Systems.</p>
  </div>

  <p class="abs proof"><strong>Already trusted by QHM communities.</strong><br>Ask your peers at The Harwick and The Olsen at Birchfield.</p>

  <p class="abs cta"><span class="accent">Book a free walkthrough</span> of your community.</p>

  <div class="abs contact contact-phone">
    <svg width="30" height="30" viewBox="0 0 24 24" aria-hidden="true"><path d="M6.6 10.8a15 15 0 0 0 6.6 6.6l2.2-2.2a1 1 0 0 1 1-.25 11.4 11.4 0 0 0 3.6.57 1 1 0 0 1 1 1V20a1 1 0 0 1-1 1A17 17 0 0 1 3 4a1 1 0 0 1 1-1h3.5a1 1 0 0 1 1 1c0 1.25.2 2.45.57 3.57a1 1 0 0 1-.25 1z" fill="#f7c514"/></svg>
    <span>512-555-0147</span>
  </div>
  <div class="abs contact contact-email">
    <svg width="30" height="22" viewBox="0 0 32 24" aria-hidden="true"><rect x="1" y="1" width="30" height="22" rx="2" fill="none" stroke="#f7c514" stroke-width="2.4"/><path d="M2 3 L16 14 L30 3" fill="none" stroke="#f7c514" stroke-width="2.4" stroke-linejoin="round"/></svg>
    <span>support@veltocleaning.example</span>
  </div>

</main>
</body>
</html>
```